Youth Sports Banner Ad - 3x5 ft banner special!

We are looking for a full page ad (8.5x11") to advertise our banner services for Youth Sports leagues. The flyers will be handed out to teams and parents in hopes to draw their business to us for team banners.
We want to show our logo, address (4187 Verbena Ln. Paso Robles). Please include that we are offering a youth sports special price on 3x5 ft team banners for $115 (plus tax). The pricing will include 1 layout with up to 2 revisions. We would like the ad to grab the attention of the audience and ask them to "Call, Email or Stop in Today!"

Our info that needs to be on the banner includes:
email: info@markwell47.net
phone: 805-291-6583

We want to really focus on our quick turnaround as we will be producing the banners withing 1-2 business days after artwork approval.
We would like to include the banner samples if possible, and if you see fit, also include that we would like the potential customer to email us their teams name, roster, and colors to help speed up the layout process.

Target Market(s)

Parents of kids playing youth sports. The flyer is meant to increase awareness of our sign shop, while offering a great discount on banners for youth sports banners.

Font styles to use
Sans Serif

Colors

Designer to choose colors to be used in the design.

Requirements
Must have
• Our logo, $115 plus tax banner price, our business information, request to send over all team information including name, roster, and team colors.
Nice to have
• Would like to see color in the ad! If you can tie in the Kelly green from our logo, that would be great.

```html
<!DOCTYPE html>
<html lang="en">
<head>
<meta charset="utf-8">
<title>Markwell Signs – Youth Sports Banner Special</title>
<link rel="stylesheet" href="https://fonts.googleapis.com/css2?family=Oswald:wght@500;600&family=Roboto+Condensed:wght@400;700&display=swap">
<style>
  :root {
    --kelly: #1f9e3a;
    --kelly-box: #3aaa5c;
    --ink: #111111;
    --slate: #6b6b6b;
    --paper: #ffffff;
    --rule: #333333;
    --panther-orange: #e8801e;
    --bandit-blue: #3b2f8f;
  }
  * { margin: 0; padding: 0; box-sizing: border-box; }
  html, body { width: 928px; height: 1200px; overflow: hidden; background: var(--paper); }
  .flyer { position: relative; width: 928px; height: 1200px; background: var(--paper); color: var(--ink);
    font-family: "Roboto Condensed", Arial, sans-serif; }

  .brand { position: absolute; left: 70px; top: 130px; width: 330px; color: var(--kelly);
    font-family: "Oswald", Impact, sans-serif; font-weight: 600; font-size: 70px; line-height: 1.08; letter-spacing: 0.5px; }

  .headline { position: absolute; left: 432px; top: 54px; font-family: "Oswald", Impact, sans-serif;
    font-weight: 600; font-size: 66px; line-height: 1.12; letter-spacing: 0.5px; }
  .header-rule { position: absolute; left: 410px; top: 246px; width: 518px; height: 6px; background: var(--ink); }
  .contact-phone { position: absolute; left: 432px; top: 262px; font-family: "Oswald", Impact, sans-serif;
    font-weight: 500; font-size: 68px; line-height: 1; }
  .contact-line { position: absolute; left: 434px; font-size: 34px; line-height: 1; }
  .contact-email { top: 356px; }
  .contact-address { top: 404px; }

  .step { position: absolute; top: 489px; width: 283px; height: 259px; background: var(--slate); color: var(--paper);
    text-align: center; font-size: 23px; line-height: 1.3; padding: 0 22px; }
  .step b { font-weight: 700; }
  .step svg { display: block; margin: 22px auto 16px; }
  .step-decide { left: 21px; }
  .step-contact { left: 317px; }
  .turnaround { position: absolute; left: 613px; top: 489px; width: 283px; height: 259px; background: var(--kelly-box);
    color: var(--paper); text-align: center; font-family: "Oswald", Impact, sans-serif; font-weight: 500;
    font-size: 40px; line-height: 1.2; padding-top: 24px; }
  .turnaround small { position: absolute; right: 8px; bottom: 6px; font-family: "Roboto Condensed", Arial, sans-serif;
    font-size: 10px; font-weight: 400; line-height: 1; }

  .special-title { position: absolute; left: 21px; top: 766px; color: var(--kelly); font-family: "Oswald", Impact, sans-serif;
    font-weight: 600; font-size: 60px; line-height: 1; }
  .special-price { position: absolute; left: 628px; top: 770px; font-size: 22px; line-height: 1.15; }
  .special-price .price-note { font-size: 18px; }

  .rule { position: absolute; left: 21px; width: 875px; height: 2px; background: var(--rule); }
  .rule-top { top: 851px; }
  .rule-bottom { top: 1136px; }
  .examples-caption { position: absolute; left: 0; width: 928px; top: 860px; text-align: center; font-size: 14px; }

  .sample-banner { position: absolute; top: 885px; width: 392px; height: 230px; box-shadow: 0 3px 6px rgba(0,0,0,.35); }
  .sample-panthers { left: 63px; background: linear-gradient(135deg, #141414 55%, var(--panther-orange)); }
  .sample-bandits { left: 473px; background: radial-gradient(circle at 50% 45%, #5a4fb5, var(--bandit-blue) 70%); }

  .footer { position: absolute; left: 0; width: 928px; top: 1156px; text-align: center; font-size: 19px; }
  .footer b { font-weight: 700; }
</style>
</head>
<body>
<main class="flyer">
  <div class="brand">MARKWELL<br>SIGNS</div>

  <h1 class="headline">CALL, EMAIL OR<br>STOP IN TODAY!</h1>
  <div class="header-rule"></div>
  <div class="contact-phone">805-291-6583</div>
  <div class="contact-line contact-email">info@markwell47.net</div>
  <div class="contact-line contact-address">4187 Verbena Ln. Paso Robles</div>

  <section class="step step-decide">
    <svg width="78" height="78" viewBox="0 0 78 78" aria-hidden="true"><circle cx="39" cy="39" r="37" fill="#ffffff"/></svg>
    <p><b>Decide</b> on what you require, no job is too big or too small for our dedicated team!</p>
  </section>
  <section class="step step-contact">
    <svg width="100" height="78" viewBox="0 0 100 70" aria-hidden="true">
      <rect x="2" y="2" width="96" height="66" fill="#ffffff"/>
      <polyline points="2,2 50,40 98,2" fill="none" stroke="#6b6b6b" stroke-width="3"/>
    </svg>
    <p><b>Contact us</b> with your team name, roster, and colors to start our layout process.</p>
  </section>
  <section class="turnaround">YOUR BANNER<br>IS READY IN<br>1-2 BUSINESS<br>DAYS!*<small>*after artwork approval.</small></section>

  <h2 class="special-title">YOUTH SPORTS SPECIAL!</h2>
  <p class="special-price">3x5 ft team banners for <b>$115!</b><br><span class="price-note">(plus tax, includes 1 layout,<br>max 2 revisions)</span></p>

  <div class="rule rule-top"></div>
  <p class="examples-caption">Examples from our satisfied customers</p>
  <div class="sample-banner sample-panthers" role="img" aria-label="Sample team banner: black and orange panther mascot banner with team name and player roster"></div>
  <div class="sample-banner sample-bandits" role="img" aria-label="Sample team banner: blue and purple bandit soccer mascot banner with numbered player roster"></div>

  <div class="rule rule-bottom"></div>
  <p class="footer"><b>MARKWELL SIGNS</b> &bull; 805-291-6583 &bull; info@markwell47.net &bull; 4187 Verbena Ln. Paso Robles</p>
</main>
</body>
</html>
```